Korbin Ventilation's. "We're Dalton beyond the pack"!

Good day< Does your company do face mask? that is question 1. and lets finish the stationary design and I will pay for that now? 2 If your company has BLACK HATS now I would want to do some of those? 3 I notice do you do BANNER'S and or something I can put on van's magnet type or on a building! )k that's enough but for now lets start with the stationary stuff? let me know you should have my information, and the design look's GREAT!!! Thank you..

```html
<!DOCTYPE html>
<html lang="en">
<head>
<meta charset="utf-8">
<title>Korbin Ventilation's – Letterhead</title>
<link href="https://fonts.googleapis.com/css2?family=Open+Sans:wght@400;600;700&display=swap" rel="stylesheet">
<style>
  :root {
    --backdrop: #d9d9d9;
    --paper: #ffffff;
    --ink: #111111;
    --body-text: #555555;
    --heading-text: #333333;
    --watermark: #e6e6e6;
    --accent: #cfea4a;
    --footer-text: #ffffff;
  }
  * { box-sizing: border-box; margin: 0; padding: 0; }
  html, body {
    width: 1040px; height: 1200px; overflow: hidden;
    background: var(--backdrop);
    font-family: "Open Sans", Arial, sans-serif;
  }
  .letterhead {
    position: absolute; left: 70px; top: 21px;
    width: 900px; height: 1158px;
    background: var(--paper);
    overflow: hidden;
    box-shadow: 0 4px 18px rgba(0,0,0,0.18);
  }
  .watermark-disc { position: absolute; left: 244px; top: 373px; }
  .brand {
    position: absolute; left: 0; right: 0; top: 30px;
    text-align: center; color: var(--ink);
  }
  .brand-mark { display: block; margin: 0 auto 8px; }
  .brand-name { font-size: 25px; font-weight: 700; line-height: 1.15; }
  .brand-tagline { font-size: 14px; font-weight: 700; margin-top: 2px; }
  .letter {
    position: absolute; left: 84px; width: 728px; top: 207px;
    color: var(--body-text); font-size: 14px;
  }
  .letter-date { margin-bottom: 18px; }
  .recipient { line-height: 17px; }
  .salutation { margin-top: 48px; }
  .letter-body p {
    margin-top: 26px; line-height: 26px; text-align: justify; hyphens: auto;
    font-size: 13.5px;
  }
  .closing { margin-top: 60px; }
  .signatory { margin-top: 58px; }
  .signatory-name { font-size: 18px; font-weight: 600; color: var(--heading-text); }
  .signatory-role { margin-top: 4px; }
  .footer-band {
    position: absolute; left: 0; right: 0; bottom: 0; height: 74px;
    background: var(--ink); color: var(--footer-text);
    text-align: center; font-size: 15px;
  }
  .footer-address { padding-top: 9px; line-height: 20px; }
  .footer-rule {
    width: 488px; height: 2px; background: var(--accent);
    margin: 6px auto 5px;
  }
  .footer-contact { line-height: 20px; }
  .footer-contact .label, .footer-contact .highlight { color: var(--accent); }
  .corner-disc { position: absolute; right: -110px; bottom: -30px; }
</style>
</head>
<body>
  <main class="letterhead">
    <svg class="watermark-disc" width="410" height="410" viewBox="0 0 410 410" aria-hidden="true">
      <circle cx="205" cy="205" r="205" fill="var(--watermark)"/>
    </svg>

    <header class="brand">
      <svg class="brand-mark" width="56" height="56" viewBox="0 0 56 56" aria-hidden="true">
        <circle cx="28" cy="28" r="28" fill="var(--ink)"/>
      </svg>
      <div class="brand-name">Korbin Ventilation's</div>
      <div class="brand-tagline">"We're Dalton beyond the pack"</div>
    </header>

    <section class="letter">
      <p class="letter-date">Issuing Date: May 5, 2018</p>
      <address class="recipient" style="font-style:normal">
        Name Of Employee Mr. XYZABC<br>
        Address of Employee<br>
        Address Line 2 etc..
      </address>
      <p class="salutation">Dear Mr.XYZABC</p>
      <div class="letter-body">
        <p>Lorem Ipsum has been the industry's standard dummy text ever since the 1500s, when an unknown printer took a galley of type and scrambled it to make a type specimen book. It has survived not only five centuries, but also the leap into electronic typesetting, remaining essentially unchanged. It was popularised in the 1960s with the release of Letraset sheets containing Lorem Ipsum passages, and more recently with desktop publishing software like Aldus PageMaker including versions of Lorem Ipsum.</p>
        <p>Lorem Ipsum is simply dummy text of the printing and typesetting industry. Lorem Ipsum has been the industry's standard dummy text ever since the 1500s, when an unknown printer took a galley of type and scrambled it to make a type specimen book.</p>
        <p>It has survived not only five centuries, but also the leap into electronic typesetting, remaining essentially unchanged. It was popularised in the 1960s with the release of Letraset sheets containing Lorem IpsumIpsum passages.</p>
      </div>
      <p class="closing">Yours Sincerely</p>
      <div class="signatory">
        <p class="signatory-name">Marcus Hale</p>
        <p class="signatory-role">Managing Director</p>
      </div>
    </section>

    <footer class="footer-band">
      <p class="footer-address">88 Ridgeway Lane, Unit 4, Dalton 30721 United States</p>
      <div class="footer-rule"></div>
      <p class="footer-contact"><span class="label">P:</span> 044-555 010 234 &nbsp;| <span class="label">E:</span> info@korbinvent.com | www.<span class="highlight">korbinvent</span>.com</p>
    </footer>

    <svg class="corner-disc" width="200" height="200" viewBox="0 0 200 200" aria-hidden="true">
      <circle cx="100" cy="100" r="98" fill="var(--ink)"/>
      <circle cx="100" cy="100" r="86" fill="none" stroke="var(--paper)" stroke-width="4"/>
    </svg>
  </main>
</body>
</html>
```